Harold T. Wexley, MD

I would like to set up a web page for my new psychiatric practice. It should summarize my credentials and approach to care plus a patient portal to complete forms before appointments.
I am uploading a powerpoint with my contact information along with the color palette and format I would like to use. The email on the slide has not been reserved and I will need to reserve the domain as part of this process.

```html
<!DOCTYPE html>
<html lang="en">
<head>
<meta charset="utf-8">
<title>Harold T. Wexley, MD, Inc</title>
<link href="https://fonts.googleapis.com/css2?family=Raleway:wght@400;500;600&family=Open+Sans:wght@400;600;700&display=swap" rel="stylesheet">
<style>
:root{
  --blue:#1a7fe8;
  --footer:#1178f0;
  --footer-bottom:#0f6fe2;
  --ink:#222;
  --text:#444;
  --muted:#8a8a8a;
  --line:#d6d6d6;
  --band:#f3f3f4;
  --white:#fff;
  --blog-red:#e8321c;
}
*{margin:0;padding:0;box-sizing:border-box}
html,body{width:827px;height:1200px;overflow:hidden;background:var(--white)}
body{position:relative;font-family:"Open Sans",Arial,sans-serif;color:var(--text)}
.abs{position:absolute}

/* header */
.site-header{left:0;top:0;width:827px;height:70px;background:var(--white)}
.brand{left:106px;top:23px;font-family:"Raleway",Arial,sans-serif;font-size:20px;color:var(--blue);font-weight:400;letter-spacing:.2px}
.main-nav a{position:absolute;top:32px;font-size:9px;color:var(--ink);text-decoration:none}
.main-nav a.active{color:var(--blue)}
.nav-underline{left:361px;top:68px;width:38px;height:2px;background:var(--blue)}

/* hero */
.hero{left:0;top:70px;width:827px;height:348px;background:radial-gradient(ellipse at 62% 30%,#bfe3ff 0%,#7fc2f2 14%,#dfe6ee 32%,#d9c9c4 55%,#c4c6cc 78%,#aeb3ba 100%)}
.hero-arrow{top:216px}
.welcome-tag{left:106px;top:171px;width:83px;height:24px;background:#2aa0f0;color:var(--white);font-family:"Raleway",Arial,sans-serif;font-size:12px;line-height:24px;text-align:center}
.welcome-box{left:106px;top:195px;width:244px;height:108px;background:rgba(255,255,255,.82);border-left:1px solid #2aa0f0}
.welcome-box h1{position:absolute;left:23px;top:15px;font-family:"Raleway",Arial,sans-serif;font-weight:400;font-size:20px;color:#111;line-height:22px;white-space:nowrap}
.welcome-box h2{position:absolute;left:23px;top:40px;font-family:"Raleway",Arial,sans-serif;font-weight:400;font-size:17px;color:#777;line-height:20px}
.welcome-box p{position:absolute;left:25px;top:67px;font-size:7.8px;line-height:13px;color:#777;width:200px}

/* services band */
.services-band{left:0;top:418px;width:827px;height:344px;background:linear-gradient(180deg,#fff 0%,var(--band) 40%,#f5f5f6 100%)}

/* feature cards */
.card{top:386px;width:198px;height:119px;color:var(--white);padding:18px 8px 0 20px}
.card h3{font-family:"Raleway",Arial,sans-serif;font-weight:400;font-size:13px;margin-bottom:6px;letter-spacing:.1px;white-space:nowrap;line-height:16px}
.card p{font-size:7.6px;line-height:13px;opacity:.88;width:160px}
.card .more{position:absolute;left:21px;top:89px;font-size:7.5px;font-weight:700;padding-bottom:2px;border-bottom:1px solid #fff}
.card-red{left:106px;background:linear-gradient(135deg,#ff5a1a,#ec2e08)}
.card-orange{left:314px;background:linear-gradient(135deg,#ffa62b,#f78a10)}
.card-blue{left:522px;background:linear-gradient(135deg,#2b8ff5,#0a68ef)}

/* services */
.section-title{left:0;top:537px;width:827px;text-align:center;font-family:"Raleway",Arial,sans-serif;font-weight:400;font-size:16px;color:#333}
.title-rule{top:547px;height:1px;background:var(--line)}
.service{top:580px;width:150px;text-align:center}
.service .ring{width:72px;height:72px;border-radius:50%;border:2px solid #dcdcdc;background:var(--white);margin:0 auto;display:flex;align-items:center;justify-content:center}
.service h4{font-family:"Raleway",Arial,sans-serif;font-weight:600;font-size:9.6px;color:#333;margin-top:13px}
.service p{font-size:7.6px;line-height:13px;color:var(--muted);margin:3px auto 0;width:126px}

/* about */
.about-title{left:110px;top:793px;font-family:"Raleway",Arial,sans-serif;font-weight:400;font-size:16px;color:var(--blue)}
.about-photo{left:110px;top:830px;width:144px;height:126px;background:linear-gradient(160deg,#e9eef3,#cfd8e0 60%,#b9c6d2)}
.about-lead{left:266px;top:827px;width:188px;font-size:8.8px;line-height:13px;color:#333}
.about-body{left:266px;top:858px;width:182px;font-size:7.6px;line-height:13px;color:var(--muted)}
.btn-more{left:266px;top:933px;width:71px;height:21px;background:linear-gradient(#fba33a,#f78d14);color:var(--white);font-size:7.6px;text-align:center;line-height:21px;border-radius:2px}

/* blogs */
.blogs-title{left:472px;top:793px;font-family:"Raleway",Arial,sans-serif;font-weight:400;font-size:16px;color:var(--blog-red)}
.blog-thumb{left:474px;width:102px;height:59px}
.thumb-one{top:826px;background:linear-gradient(135deg,#c9cdd3,#6d747d 55%,#e7e8ea)}
.thumb-two{top:899px;background:radial-gradient(circle at 55% 45%,#c8243a 0%,#3a4b6a 30%,#0f1522 75%)}
.blog-item{left:584px;width:136px}
.blog-item h5{font-weight:400;font-size:8.8px;color:#333}
.blog-item p{font-size:7px;line-height:11.5px;color:var(--muted);margin-top:2px}
.blog-item a{display:block;font-size:7px;font-weight:600;color:var(--blue);text-decoration:none;margin-top:5px}

/* footer */
.site-footer{left:0;top:1007px;width:827px;height:193px;background:linear-gradient(160deg,#1a84f4 0%,var(--footer) 55%,#0c6fee 100%);color:var(--white)}
.footer-col{top:34px}
.footer-col h6{font-family:"Raleway",Arial,sans-serif;font-weight:400;font-size:11.5px;margin-bottom:7px}
.footer-col li{list-style:none;font-size:8.4px;line-height:16px}
.social{display:flex;gap:3px;margin-top:2px}
.social span{width:21px;height:21px;border:1px solid #fff;border-radius:50%}
.footer-bottom{left:0;top:159px;width:827px;height:34px;background:var(--footer-bottom);border-top:1px solid rgba(255,255,255,.18)}
.footer-bottom p{position:absolute;left:106px;top:10px;font-size:7px;opacity:.9}
.contact-line{display:flex;align-items:center;gap:5px}
</style>
</head>
<body>

<header class="abs site-header">
  <div class="abs brand">Harold T. Wexley, MD, Inc</div>
  <nav class="main-nav">
    <a class="active" style="left:366px">HOME</a>
    <a style="left:410px">ABOUT US</a>
    <a style="left:475px">PRACTISE</a>
    <a style="left:536px">SERVICES</a>
    <a style="left:597px">TESTIMONIAL</a>
    <a style="left:676px">CONTACT</a>
  </nav>
  <div class="abs nav-underline"></div>
</header>

<section class="abs hero" role="img" aria-label="Cupped hands holding a glowing blue brain"></section>
<svg class="abs hero-arrow" style="left:72px" width="14" height="28" viewBox="0 0 14 28"><path d="M12 3 L3 14 L12 25" fill="none" stroke="#1a7fe8" stroke-width="2.6"/></svg>
<svg class="abs hero-arrow" style="left:745px" width="14" height="28" viewBox="0 0 14 28"><path d="M2 3 L11 14 L2 25" fill="none" stroke="#1a7fe8" stroke-width="2.6"/></svg>

<div class="abs welcome-tag">WELCOME</div>
<div class="abs welcome-box">
  <h1>SOLO PSYCHIATRIC</h1>
  <h2>PRACTITIONER</h2>
  <p>Donec quis mi sed magna hendrerit accumsan<br>Susp endisse risus nibh ultricies eu</p>
</div>

<div class="abs services-band"></div>

<article class="abs card card-red">
  <h3>WHAT WE DO</h3>
  <p>Donec quis mi sed magna hendrerit accumsan Suspendisse risus nibh ultricies eu volutpat non condimentum</p>
  <span class="more">READ MORE</span>
</article>
<article class="abs card card-orange">
  <h3>PSYCHIATRIC TREATMENT</h3>
  <p>Donec quis mi sed magna hendrerit accumsan Suspendisse risus nibh ultricies eu volutpat non condimentum</p>
  <span class="more">READ MORE</span>
</article>
<article class="abs card card-blue">
  <h3>OUR PRACTICE</h3>
  <p>Donec quis mi sed magna hendrerit accumsan Suspendisse risus nibh ultricies eu volutpat non condimentum</p>
  <span class="more">READ MORE</span>
</article>

<div class="abs title-rule" style="left:106px;width:215px"></div>
<div class="abs title-rule" style="left:505px;width:215px"></div>
<h2 class="abs section-title">SERVICES PROVIDES</h2>

<div class="abs service" style="left:112px">
  <div class="ring">
    <svg width="32" height="34" viewBox="0 0 32 34"><path d="M6 3 V13 a7 7 0 0 0 14 0 V3" fill="none" stroke="#1a7fe8" stroke-width="2.6"/><path d="M13 20 V24 a6 6 0 0 0 12 0 V18" fill="none" stroke="#1a7fe8" stroke-width="2.6"/><circle cx="25" cy="14" r="3.4" fill="none" stroke="#1a7fe8" stroke-width="2.4"/></svg>
  </div>
  <h4>TREATMENT</h4>
  <p>Donec quis mi sed magna hendrerit accumsan Suspendisse risus nibh ultricies</p>
</div>
<div class="abs service" style="left:262px">
  <div class="ring">
    <svg width="42" height="36" viewBox="0 0 42 36"><path d="M6 20 C1 17 3 9 9 9 C9 3 17 1 20 5 C23 1 31 2 32 7 C38 7 41 14 37 18 C41 23 36 29 31 27 L28 27 L28 34 L21 34 L21 28 C15 30 11 28 10 25 C5 26 3 22 6 20 Z" fill="#1a7fe8"/><path d="M14 12 C17 14 17 18 14 20 M22 9 C24 13 27 13 28 16 M20 19 C23 21 26 21 28 23" fill="none" stroke="#fff" stroke-width="1.4"/></svg>
  </div>
  <h4>OUR RESEARCH</h4>
  <p>Donec quis mi sed magna hendrerit accumsan Suspendisse risus nibh ultricies</p>
</div>
<div class="abs service" style="left:412px">
  <div class="ring">
    <svg width="34" height="34" viewBox="0 0 34 34"><circle cx="13" cy="4" r="3" fill="#1a7fe8"/><path d="M13 9 V19 H23 L27 28" fill="none" stroke="#1a7fe8" stroke-width="2.8"/><path d="M9 14 a9 9 0 1 0 12 12" fill="none" stroke="#1a7fe8" stroke-width="2.6"/></svg>
  </div>
  <h4>OUR PATIENTS</h4>
  <p>Donec quis mi sed magna hendrerit accumsan Suspendisse risus nibh ultricies</p>
</div>
<div class="abs service" style="left:563px">
  <div class="ring">
    <svg width="30" height="26" viewBox="0 0 30 26"><ellipse cx="15" cy="10" rx="14" ry="9.5" fill="#1a7fe8"/><path d="M6 16 L3 24 L13 18 Z" fill="#1a7fe8"/></svg>
  </div>
  <h4>CONSULTING</h4>
  <p>Donec quis mi sed magna hendrerit accumsan Suspendisse risus nibh ultricies</p>
</div>

<h2 class="abs about-title">About Harold T. Wexley</h2>
<div class="abs about-photo" role="img" aria-label="Portrait of the doctor in a white coat with a stethoscope"></div>
<p class="abs about-lead">Duis sed tellus et tortor vestibulum gravida Praesent elementum elit at</p>
<p class="abs about-body">Donec quis mi sed magna hendrerit accumsan Suspendisse risus nibh ultricies eu volutpat non condimentum hendrerit augue<br>Etiam eleifend metus vitae adipiscing semper mauris ipsum iaculis elit congue gravida elit mi</p>
<div class="abs btn-more">READ MORE</div>

<h2 class="abs blogs-title">Recent Blogs</h2>
<div class="abs blog-thumb thumb-one" role="img" aria-label="Stressed man lying on a couch"></div>
<div class="abs blog-item" style="top:826px">
  <h5>Aies eu volutpat non</h5>
  <p>In massa libero interdum nec interdum<br>vel blandit sed nulla In ullam</p>
  <a>READ MORE</a>
</div>
<div class="abs blog-thumb thumb-two" role="img" aria-label="Brain scan with a highlighted red region"></div>
<div class="abs blog-item" style="top:899px">
  <h5>Vestibulum ligula augue</h5>
  <p>In massa libero interdum nec interdum<br>vel blandit sed nulla In ullam</p>
  <a>READ MORE</a>
</div>

<footer class="abs site-footer">
  <div class="abs footer-col" style="left:106px">
    <h6>COMPANY</h6>
    <ul><li>Home</li><li>About Us</li><li>What We Do</li><li>Our Practice</li></ul>
  </div>
  <div class="abs footer-col" style="left:214px">
    <h6>SERVICES</h6>
    <ul><li>Treatment &amp; Care</li><li>Pellentesque</li><li>Faucibus Ut</li><li>Accumsan</li></ul>
  </div>
  <div class="abs footer-col" style="left:328px;top:32px">
    <h6>RESOURCES</h6>
    <ul><li>Blog Post</li><li>Testimonials</li><li>Contact Us</li></ul>
  </div>
  <div class="abs footer-col" style="left:438px">
    <h6>CONTACT INFO</h6>
    <ul>
      <li>PO Box 4120 Suite 77 Alder</li>
      <li>Grove, CA 90000</li>
      <li class="contact-line" style="margin-top:5px"><svg width="10" height="10" viewBox="0 0 10 10"><path d="M2 1 L4 3 L3 4.5 C4 6 5 7 6.5 7.5 L8 6.5 L9.5 8.5 L8 9.5 C4 9 1 6 0.8 2 Z" fill="none" stroke="#fff" stroke-width="0.9"/></svg>555-014-2290</li>
      <li class="contact-line"><svg width="10" height="8" viewBox="0 0 10 8"><rect x="0.5" y="0.5" width="9" height="7" fill="#fff"/><path d="M0.5 0.8 L5 4.5 L9.5 0.8" fill="none" stroke="#1178f0" stroke-width="0.9"/></svg>harold@hwexleymd.com</li>
    </ul>
  </div>
  <div class="abs footer-col" style="left:603px">
    <h6>FOLLOW US</h6>
    <div class="social"><span></span><span></span><span></span><span></span></div>
  </div>
  <div class="abs footer-bottom"><p>© 2016 Company Name &nbsp;All right reserved &nbsp;Term of Use</p></div>
</footer>

</body>
</html>
```